VERIDAX Need a luxury modern business card designed.

Need a luxury modern business card designed. refer to the uploaded files for the company name and logo in the zip file under source files. i will making my descion on monday. so please send in before then so if we need to edit we will have the time. we have a trade show coming up and im on a deadline for printer.

Target Market(s)

high end clients

Contact Information for Business Card

Company nAme and logo. Calvin Ostrow Co-Founder / Project Manager Office # 416-555-0193 Cell # 416-555-0147 VERIDAX.CA Calvin@veridax.ca

Font styles to use
Other font styles liked:
• Modern

Requirements
Must have
• Company name and logo, contact info, using the black, gold and white color scheme.

```html
<!DOCTYPE html>
<html lang="en">
<head>
<meta charset="utf-8">
<title>VERIDAX Business Card</title>
<link rel="stylesheet" href="https://fonts.googleapis.com/css2?family=Open+Sans:wght@300;400;600&family=Oswald:wght@500&display=swap">
<style>
  :root {
    --stage: #252525;
    --card: #333333;
    --gold: #b3a06a;
    --gold-edge: #a8976a;
    --white: #f4f4f2;
    --muted: #d8d8d4;
  }
  * { box-sizing: border-box; margin: 0; padding: 0; }
  html, body {
    width: 1200px; height: 895px; overflow: hidden;
    background: var(--stage);
    font-family: "Open Sans", Arial, sans-serif;
  }
  .stage {
    width: 1200px; height: 895px;
    display: flex; flex-direction: column; align-items: center; justify-content: center;
    gap: 44px;
  }
  .card {
    position: relative;
    width: 665px; height: 380px;
    background: var(--card);
    border-radius: 22px;
    box-shadow: 0 4px 0 var(--gold-edge), 0 14px 30px rgba(0,0,0,.45);
    overflow: hidden;
  }

  /* Front */
  .card-front {
    display: flex; flex-direction: column; align-items: center; justify-content: center;
  }
  .brand { display: flex; align-items: center; gap: 16px; }
  .brand-mark { width: 22px; height: 22px; background: var(--gold); }
  .brand-name {
    font-weight: 300; font-size: 50px; letter-spacing: 12px;
    color: var(--white);
  }
  .front-web {
    margin-top: 34px;
    font-size: 19px; color: var(--white); letter-spacing: .5px;
  }

  /* Back */
  .card-back .identity {
    position: absolute; right: 265px; top: 112px;
    text-align: right;
  }
  .person-name {
    font-family: "Oswald", "Arial Narrow", sans-serif;
    font-weight: 500; font-size: 48px; line-height: 1;
    color: var(--white); text-transform: uppercase; letter-spacing: .5px;
    white-space: nowrap;
  }
  .person-role {
    margin-top: 6px;
    font-weight: 300; font-size: 16px; color: var(--gold);
    white-space: nowrap;
  }
  .divider {
    position: absolute; left: 420px; top: 100px;
    width: 1.5px; height: 112px; background: var(--white);
  }
  .contacts {
    position: absolute; left: 440px; top: 98px;
    list-style: none;
  }
  .contacts li {
    display: flex; align-items: center; gap: 12px;
    font-size: 16px; color: var(--white); line-height: 29px;
    white-space: nowrap;
  }
  .contacts svg { width: 16px; height: 16px; flex: none; }
  .contacts .accent { color: var(--gold); }
  .address {
    position: absolute; left: 0; right: 0; bottom: 52px;
    text-align: center;
    font-size: 19px; color: var(--muted); letter-spacing: .3px;
  }
</style>
</head>
<body>
<main class="stage">

  <section class="card card-front" aria-label="Card front">
    <div class="brand">
      <span class="brand-mark"></span>
      <span class="brand-name">VERIDAX</span>
    </div>
    <p class="front-web">www.veridax.ca</p>
  </section>

  <section class="card card-back" aria-label="Card back">
    <div class="identity">
      <h1 class="person-name">Calvin Ostrow</h1>
      <p class="person-role">Co-Founder / Project Manager</p>
    </div>
    <span class="divider"></span>
    <ul class="contacts">
      <li>
        <svg viewBox="0 0 16 16" fill="none" stroke="#b3a06a" stroke-width="1.5"><path d="M3 2.5h3l1 3-2 1.2a8 8 0 0 0 4.3 4.3L10.5 9l3 1v3a1.2 1.2 0 0 1-1.3 1.2A11 11 0 0 1 1.8 3.8 1.2 1.2 0 0 1 3 2.5z"/></svg>
        <span>416-555-0193</span>
      </li>
      <li>
        <svg viewBox="0 0 16 16" fill="none" stroke="#b3a06a" stroke-width="1.6"><rect x="4" y="1" width="8" height="14" rx="1.5"/><line x1="7" y1="12.5" x2="9" y2="12.5"/></svg>
        <span>416-555-0147</span>
      </li>
      <li>
        <svg viewBox="0 0 16 16" fill="none" stroke="#b3a06a" stroke-width="1.6"><rect x="1" y="3" width="14" height="10" rx="1"/><polyline points="1.5,3.5 8,9 14.5,3.5"/></svg>
        <span>Calvin@<span class="accent">veridax.ca</span></span>
      </li>
      <li>
        <svg viewBox="0 0 16 16" fill="none" stroke="#b3a06a" stroke-width="1.8"><circle cx="9.5" cy="6.5" r="4.5"/><line x1="6.3" y1="9.7" x2="1.5" y2="14.5"/></svg>
        <span>www.<span class="accent">veridax.ca</span></span>
      </li>
    </ul>
    <p class="address">48 Marlow Road. Unit 5, Concord, ON. L4K 2B7</p>
  </section>

</main>
</body>
</html>
```